New Plumbing Company

We are looking for a smart and creative business card design for our new plumbing company. We are looking for creativity and originality in our business cards.

Industry/Entity Type

Plumbing

Contact Information for Business Card

Crestline Plumbing
Peter Halvane
Managing Director
Telephone Number : 0481529604
Email : service@crestlineplumbing.com.au
Website : www.crestlineplumbing.com.au
Lic. 508264K

Colors
0692cd
33a6d7
000000

Requirements
Must have
• I want the business card to be designed on a black background using the blue tones i have selected as seen in the company logo.

```html
<!DOCTYPE html>
<html lang="en">
<head>
<meta charset="utf-8">
<title>Crestline Plumbing – Business Card</title>
<link href="https://fonts.googleapis.com/css2?family=Arimo:wght@400;700&display=swap" rel="stylesheet">
<style>
  :root {
    --brand-blue: #0692cd;
    --accent-blue: #33a6d7;
    --card-black: #000000;
    --card-surface: #0b0b0c;
    --band-grey: #3a3a3d;
    --text-white: #ffffff;
    --text-soft: #d9d9d9;
    --stage: #bfbfc1;
  }
  * { box-sizing: border-box; margin: 0; padding: 0; }
  html, body { width: 1200px; height: 960px; overflow: hidden; }
  body {
    background: radial-gradient(circle at 35% 30%, #ececec 0%, var(--stage) 60%, #8e8e90 100%);
    font-family: "Arimo", Arial, sans-serif;
    display: flex;
    align-items: center;
    justify-content: center;
    gap: 40px;
  }
  .card {
    position: relative;
    width: 540px;
    height: 330px;
    background: linear-gradient(135deg, #1a1a1b 0%, var(--card-surface) 45%, var(--card-black) 100%);
    box-shadow: 0 18px 40px rgba(0,0,0,.35);
    overflow: hidden;
  }

  /* Front */
  .card--front { display: flex; align-items: center; justify-content: center; gap: 20px; }
  .brand-mark {
    width: 78px; height: 78px;
    border: 5px solid var(--brand-blue);
    border-radius: 50%;
    flex: none;
  }
  .brand-name {
    color: var(--brand-blue);
    font-weight: 400;
    font-size: 38px;
    letter-spacing: .5px;
    white-space: nowrap;
  }

  /* Back */
  .card__band { position: absolute; inset: 0; pointer-events: none; }
  .back-brand {
    position: absolute; left: 34px; top: 92px;
    display: flex; align-items: center; gap: 10px;
  }
  .back-brand .brand-mark { width: 34px; height: 34px; border-width: 3px; }
  .back-brand .brand-name { font-size: 17px; }
  .licence {
    position: absolute; left: 56px; top: 190px;
    color: var(--text-white); font-size: 13px;
  }
  .person { position: absolute; left: 300px; top: 50px; }
  .person__name { color: var(--accent-blue); font-weight: 700; font-size: 24px; }
  .person__role { color: var(--text-soft); font-size: 13px; margin-top: 6px; }
  .contacts { position: absolute; left: 262px; top: 140px; list-style: none; }
  .contacts li { display: flex; align-items: center; gap: 14px; height: 36px; margin-bottom: 4px; }
  .contacts .icon {
    width: 32px; height: 32px; background: var(--accent-blue);
    display: flex; align-items: center; justify-content: center; flex: none;
  }
  .contacts .label { color: var(--text-white); font-size: 13px; white-space: nowrap; }
</style>
</head>
<body>

<section class="card card--front" aria-label="Business card front">
  <span class="brand-mark" aria-hidden="true"></span>
  <span class="brand-name">Crestline Plumbing</span>
</section>

<section class="card card--back" aria-label="Business card back">
  <svg class="card__band" width="540" height="330" viewBox="0 0 540 330" aria-hidden="true">
    <defs>
      <linearGradient id="bandShade" x1="0" x2="1" y1="0" y2="0">
        <stop offset="0" stop-color="#1c1c1e"/>
        <stop offset="1" stop-color="#4a4a4e"/>
      </linearGradient>
    </defs>
    <polygon points="262,0 284,0 236,330 214,330" fill="url(#bandShade)"/>
  </svg>

  <div class="back-brand">
    <span class="brand-mark" aria-hidden="true"></span>
    <span class="brand-name">Crestline Plumbing</span>
  </div>
  <p class="licence">Lic. 508264K</p>

  <div class="person">
    <p class="person__name">Peter Halvane</p>
    <p class="person__role">Managing Director</p>
  </div>

  <ul class="contacts">
    <li>
      <span class="icon"><svg width="16" height="16" viewBox="0 0 24 24" aria-hidden="true"><path fill="#fff" d="M6.6 10.8a15.1 15.1 0 0 0 6.6 6.6l2.2-2.2a1 1 0 0 1 1-.25 11.4 11.4 0 0 0 3.6.57 1 1 0 0 1 1 1V20a1 1 0 0 1-1 1A17 17 0 0 1 3 4a1 1 0 0 1 1-1h3.5a1 1 0 0 1 1 1c0 1.25.2 2.45.57 3.57a1 1 0 0 1-.25 1z"/></svg></span>
      <span class="label">0481529604</span>
    </li>
    <li>
      <span class="icon"><svg width="16" height="16" viewBox="0 0 24 24" aria-hidden="true"><path fill="#fff" d="M12 2a7 7 0 0 0-7 7c0 5.2 7 13 7 13s7-7.8 7-13a7 7 0 0 0-7-7zm0 9.5A2.5 2.5 0 1 1 12 6.5a2.5 2.5 0 0 1 0 5z"/></svg></span>
      <span class="label">Street, City, Zip, AU</span>
    </li>
    <li>
      <span class="icon"><svg width="16" height="16" viewBox="0 0 24 24" aria-hidden="true"><rect x="3" y="5" width="18" height="14" fill="none" stroke="#fff" stroke-width="2"/><path d="M3 6l9 7 9-7" fill="none" stroke="#fff" stroke-width="2"/></svg></span>
      <span class="label">service@crestlineplumbing.com.au</span>
    </li>
    <li>
      <span class="icon"><svg width="16" height="16" viewBox="0 0 24 24" aria-hidden="true"><g fill="none" stroke="#fff" stroke-width="2"><circle cx="12" cy="12" r="9"/><ellipse cx="12" cy="12" rx="4" ry="9"/><path d="M3 12h18"/></g></svg></span>
      <span class="label">www.crestlineplumbing.com.au</span>
    </li>
  </ul>
</section>

</body>
</html>
```